New career and executive coaching business needs a business card design including logo

Company name: 'Harbourline Career Partners.' The aim of my coaching engagements is to help people improve their communication in the workplace and achieve their career goals. The process involves working with individuals to help them uncover their strengths and talents, then leverage those to improve their working lives. The Tellwood Inventory is the starting point to the process. I am after an exciting and interesting business card design (including logo)which is professional yet will still get people's attention.

Industry/Entity Type

Business

Contact Information for Business Card

Name: Gavin Holloway
Position: Owner
Address: 58 Pellimore Cres, Wardell Vic 3197
Phone: 0481937145
Website: harbourlinecareer.com.au
Email: gavin@hcp.com.au

Colors
33a6d7
00a990
0355a3
3176b5

Requirements
Must have
• logo

```html
<!DOCTYPE html>
<html lang="en">
<head>
<meta charset="utf-8">
<title>Harbourline Career Partners – Business Card</title>
<link rel="stylesheet" href="https://fonts.googleapis.com/css2?family=Open+Sans:wght@400;600;700&display=swap">
<style>
  :root {
    --backdrop: #2e3035;
    --teal: #00a990;
    --teal-card: #02ab92;
    --teal-shade: #019c85;
    --paper: #ffffff;
    --paper-edge: #f1f2f2;
    --ink: #111111;
    --muted: #2a2a2a;
  }
  * { box-sizing: border-box; margin: 0; padding: 0; }
  html, body {
    width: 1200px; height: 864px; overflow: hidden;
    background: var(--backdrop);
    font-family: "Open Sans", Arial, sans-serif;
  }
  .stage { position: relative; width: 1200px; height: 864px; }

  .card {
    position: absolute;
    width: 560px; height: 320px;
    border-radius: 3px;
    box-shadow: 0 14px 30px rgba(0,0,0,.45);
    overflow: hidden;
  }

  /* Front of card */
  .card--front {
    left: 210px; top: 70px;
    background: linear-gradient(100deg, var(--teal-shade) 0%, var(--teal-card) 45%, var(--teal-card) 100%);
  }
  .card--front .brand-name {
    position: absolute; right: 36px; bottom: 40px;
    color: var(--paper);
    font-weight: 600; font-size: 30px; line-height: 1.1;
    text-align: right;
  }

  /* Back of card */
  .card--back {
    left: 410px; top: 460px;
    background: radial-gradient(circle at 30% 40%, var(--paper) 0%, var(--paper) 55%, var(--paper-edge) 100%);
    color: var(--ink);
  }
  .brand {
    position: absolute; right: 36px; top: 46px;
    display: flex; align-items: center; gap: 12px;
  }
  .brand__mark { width: 34px; height: 34px; background: var(--teal); }
  .brand__name {
    color: var(--ink);
    font-weight: 600; font-size: 24px; line-height: 1.1;
  }
  .person { position: absolute; left: 56px; top: 160px; }
  .person__name { color: var(--teal); font-weight: 700; font-size: 19px; line-height: 1.1; }
  .person__role { font-size: 12px; color: var(--muted); line-height: 1.2; }

  .contact {
    position: absolute; right: 36px; bottom: 30px;
    list-style: none; text-align: right;
    font-size: 14px; line-height: 24px; color: var(--ink);
  }
  .contact li { display: flex; justify-content: flex-end; align-items: center; gap: 8px; }
  .contact svg { width: 12px; height: 12px; fill: var(--teal); }
  .contact .no-icon { padding-right: 20px; font-size: 15px; }
</style>
</head>
<body>
<main class="stage">
  <section class="card card--front" aria-label="Card front">
    <p class="brand-name">Harbourline<br>Career Partners</p>
  </section>

  <section class="card card--back" aria-label="Card back">
    <div class="brand">
      <span class="brand__mark"></span>
      <span class="brand__name">Harbourline Career Partners</span>
    </div>

    <div class="person">
      <p class="person__name">Gavin Holloway</p>
      <p class="person__role">Owner</p>
    </div>

    <ul class="contact">
      <li>0481937145
        <svg viewBox="0 0 24 24" aria-hidden="true"><path d="M6.6 10.8a15 15 0 0 0 6.6 6.6l2.2-2.2c.3-.3.7-.4 1-.2 1.1.4 2.3.6 3.6.6.6 0 1 .4 1 1V20c0 .6-.4 1-1 1A17 17 0 0 1 3 4c0-.6.4-1 1-1h3.5c.6 0 1 .4 1 1 0 1.3.2 2.5.6 3.6.1.3 0 .7-.2 1z"/></svg>
      </li>
      <li>gavin@hcp.com.au
        <svg viewBox="0 0 24 24" aria-hidden="true"><path d="M2 5h20v14H2z M4 7v.5l8 5 8-5V7l-8 5z" fill-rule="evenodd"/></svg>
      </li>
      <li>harbourlinecareer.com.au
        <svg viewBox="0 0 24 24" aria-hidden="true"><circle cx="12" cy="12" r="10"/></svg>
      </li>
      <li class="no-icon">58 Pellimore Cres, Wardell Vic 3197</li>
    </ul>
  </section>
</main>
</body>
</html>
```